Drone company needs a brochure design

We would like a brochure design which compliments our existing logo, website and business card designs.

www.tallowmerrin.com.au

Business

```html
<!DOCTYPE html>
<html lang="en">
<head>
<meta charset="utf-8">
<title>Tallow Merrin Brochure Spreads</title>
<link rel="stylesheet" href="https://fonts.googleapis.com/css2?family=Fira+Sans:wght@400;500;600&display=swap">
<style>
  :root {
    --ink-teal: #0e4a55;
    --brand-blue: #0a8ac4;
    --panel-blue: rgba(0, 134, 196, 0.9);
    --url-blue: #1b8fc9;
    --page: #ffffff;
    --canvas: #ffffff;
    --sky: #5bb7dd;
    --water: #1f7fb8;
    --city: #8a8f8a;
  }
  * { margin: 0; padding: 0; box-sizing: border-box; }
  html, body { width: 1200px; height: 1200px; overflow: hidden; background: var(--canvas); }
  body { position: relative; font-family: "Fira Sans", sans-serif; }

  .page { position: absolute; left: 169px; width: 881px; background: var(--page); }
  .page--contents { top: 18px; height: 622px; }
  .page--services { top: 680px; height: 510px; }

  .running-head { position: absolute; left: 47px; top: 18px; display: flex; align-items: center; height: 18px; }
  .running-head__number { font-size: 12px; font-weight: 600; color: var(--ink-teal); }
  .running-head__rule { width: 2px; height: 18px; background: var(--brand-blue); margin: 0 9px 0 12px; }
  .running-head__name { font-size: 10px; font-weight: 500; color: var(--brand-blue); }

  .contents { position: absolute; left: 45px; top: 128px; width: 390px; }
  .contents__title { font-size: 18px; font-weight: 600; color: var(--ink-teal); line-height: 22px; }
  .contents__list { list-style: none; }
  .contents__item {
    display: flex; align-items: baseline; height: 16.8px;
    font-size: 13.5px; font-variant: small-caps; color: var(--ink-teal); letter-spacing: 0.2px;
  }
  .contents__leader { flex: 1; border-bottom: 1.5px dotted var(--ink-teal); margin: 0 2px; transform: translateY(-3px); }

  .page-url { position: absolute; left: 45px; font-size: 9px; color: var(--url-blue); letter-spacing: 0.3px; }
  .page--contents .page-url { top: 571px; }
  .page--services .page-url { top: 469px; }

  .hero-photo {
    position: absolute; left: 0; top: 26px; width: 703px; height: 359px;
    background: linear-gradient(170deg, var(--sky) 0%, var(--water) 30%, #3d7f9b 50%, var(--city) 80%, #c9c7bd 100%);
  }
  .service-panel {
    position: absolute; left: 445px; top: 71px; width: 436px; height: 269px;
    background: var(--panel-blue); color: #fff; padding: 38px 42px 0 42px;
  }
  .service-panel__title { font-size: 26px; font-weight: 500; letter-spacing: 0.3px; line-height: 30px; margin-bottom: 52px; }
  .service-panel__text { font-size: 12.5px; line-height: 16px; }
  .service-panel__text + .service-panel__text { margin-top: 16px; }
</style>
</head>
<body>
  <section class="page page--contents">
    <header class="running-head">
      <span class="running-head__number">2</span>
      <span class="running-head__rule"></span>
      <span class="running-head__name">Tallow Merrin</span>
    </header>
    <nav class="contents">
      <h2 class="contents__title">CONTENTS</h2>
      <ol class="contents__list">
        <li class="contents__item"><span>Corporate Business Brochure</span><span class="contents__leader"></span><span>3</span></li>
        <li class="contents__item"><span>Services</span><span class="contents__leader"></span><span>4</span></li>
        <li class="contents__item"><span>Construction &amp; Property</span><span class="contents__leader"></span><span>5</span></li>
        <li class="contents__item"><span>Media &amp; Advertising</span><span class="contents__leader"></span><span>6</span></li>
        <li class="contents__item"><span>Inspection &amp; Environment</span><span class="contents__leader"></span><span>7</span></li>
        <li class="contents__item"><span>Survey &amp; Mapping</span><span class="contents__leader"></span><span>8</span></li>
        <li class="contents__item"><span>Insurance &amp; Risk</span><span class="contents__leader"></span><span>9</span></li>
        <li class="contents__item"><span>Our fixed line assets</span><span class="contents__leader"></span><span>10</span></li>
        <li class="contents__item"><span>Board of Directors</span><span class="contents__leader"></span><span>11</span></li>
        <li class="contents__item"><span>What we offer</span><span class="contents__leader"></span><span>12</span></li>
        <li class="contents__item"><span>Executive Committee</span><span class="contents__leader"></span><span>13</span></li>
        <li class="contents__item"><span>Five year record</span><span class="contents__leader"></span><span>14</span></li>
        <li class="contents__item"><span>Our reach and scale</span><span class="contents__leader"></span><span>15</span></li>
        <li class="contents__item"><span>Directors’ remuneration report</span><span class="contents__leader"></span><span>16</span></li>
        <li class="contents__item"><span>Supplementary information</span><span class="contents__leader"></span><span>17</span></li>
      </ol>
    </nav>
    <footer class="page-url">WWW.TALLOWMERRIN.COM.AU</footer>
  </section>

  <section class="page page--services">
    <div class="hero-photo" role="img" aria-label="Aerial drone photograph of a waterfront city centre with high-rise towers and a long suspension bridge over the bay"></div>
    <div class="service-panel">
      <h2 class="service-panel__title">SERVICES</h2>
      <p class="service-panel__text">Real Estate<br>Buyers want to learn about the area surrounding their property as much as they want to learn about the property itself.</p>
      <p class="service-panel__text">Tallow Merrin can showcase important factors like proximity to the the coast, lakes, schools, major transport, CBD and the general feel of an area.</p>
    </div>
    <footer class="page-url">WWW.TALLOWMERRIN.COM.AU</footer>
  </section>
</body>
</html>
```